we are starting an online childrens clothing store, The Kettle Beneath The Hill, and require an easy to navigate, simple and elegant in design. we will suply our own domain and company logo.

Target Market(s)

Familys with children aged 0 to 8

Industry/Entity Type

Clothing

Requirements
Must have
• easy to navigate,
our company logo on the header of each page
easy two step checkout with paypal access.
easy to modify and add to site by us at no or minimal cost.
6 pages, home page, boys clothing, girls clothing, our brands, about us, contact.
google ads
face book link
Should not have
• pop up ads
dark colours

```html
<!DOCTYPE html>
<html lang="en">
<head>
<meta charset="utf-8">
<title>Children's Clothing Store – Home</title>
<link href="https://fonts.googleapis.com/css2?family=PT+Sans:wght@400;700&family=Open+Sans:wght@400;600;700;800&display=swap" rel="stylesheet">
<style>
:root{
  --canvas:#eeeeee;
  --page:#ffffff;
  --topbar:#3d3d3d;
  --pink:#e5408f;
  --pink-dark:#b52a6c;
  --sky:#5bc8f5;
  --teal:#2bb7c4;
  --orange:#f26522;
  --red:#e53a1e;
  --text:#333333;
  --muted:#888888;
  --line:#e3e3e3;
  --sale:#e03a3a;
  --tee-teal:#1f5f66;
  --rugby-green:#1f8a3c;
  --tee-green:#3fae4f;
  --sweat-lilac:#9aa3d6;
  --dress-lilac:#b47ad8;
  --dress-plum:#4b1f6e;
  --dress-dots:#e7a3c6;
  --dress-coral:#ee6f73;
}
*{box-sizing:border-box;margin:0;padding:0}
html,body{width:766px;height:1200px;overflow:hidden}
body{background:var(--canvas);font-family:"PT Sans",Arial,sans-serif;color:var(--text);font-size:9px}
.page{position:absolute;left:69px;top:26px;width:632px;height:1160px;background:var(--page)}
.topbar{height:26px;background:var(--topbar);color:#ddd;display:flex;align-items:center;padding:0 12px;font-size:7.5px;gap:22px}
.topbar .item{display:flex;align-items:center;gap:5px}
.topbar .checkout{background:var(--sky);color:#fff;padding:2px 7px;border-radius:2px}
.topbar .welcome{margin-left:auto}
.topbar .welcome a{color:var(--sky);text-decoration:none}
.masthead{height:73px;display:flex;align-items:center;justify-content:space-between;padding:0 13px 0 14px}
.logo{font-family:"Open Sans",Arial,sans-serif;font-size:25px;line-height:21px;letter-spacing:1px;color:#222;font-weight:400}
.logo span{display:block;font-size:15px;letter-spacing:4px}
.cart{display:flex;align-items:center;gap:8px;text-align:right}
.cart .label{font-size:10px;color:#333}
.cart .count{font-size:7px;color:var(--muted)}
.cart .total{background:var(--sky);color:#fff;font-size:11.5px;padding:7px 7px;border-radius:2px}
.nav{margin:0 13px;height:24px;background:var(--pink);display:flex;align-items:center;font-size:10px;color:#fff;padding-right:4px}
.nav .home{width:24px;height:24px;display:flex;align-items:center;justify-content:center}
.nav a{color:#fff;text-decoration:none;padding:0 12px;height:24px;line-height:24px}
.nav a.active{background:var(--pink-dark)}
.nav .search{margin-left:auto;display:flex;align-items:center;gap:6px}
.nav .search .field{width:148px;height:16px;background:#fff;border:1px solid #f2b5d2;display:flex;justify-content:flex-end;align-items:center;padding-right:3px}
.hero{position:relative;margin:20px 13px 0;height:233px;background:#f6f6f6}
.hero .inner{position:absolute;left:46px;top:0;width:516px;height:233px;background:#fbfbfb}
.hero .photo{position:absolute;left:0;top:16px;width:226px;height:217px;background:linear-gradient(160deg,#e9eef3 0%,#c9d6e6 45%,#e2875f 75%,#5b6fa8 100%);border-radius:110px 110px 0 0}
.hero .brand{position:absolute;left:340px;top:14px;font-family:"Open Sans",Arial,sans-serif;font-weight:800;font-size:22px;color:var(--pink)}
.hero .headline{position:absolute;left:238px;top:70px;font-family:"Open Sans",Arial,sans-serif;font-weight:800;font-size:33px;color:var(--teal);letter-spacing:.5px}
.hero .sub{position:absolute;left:250px;top:111px;font-family:"Open Sans",Arial,sans-serif;font-weight:700;font-size:18px;color:var(--orange)}
.hero .list{position:absolute;left:257px;top:144px;font-family:"Open Sans",Arial,sans-serif;font-weight:600;font-size:10px;line-height:15px;color:#333;text-align:center;width:230px}
.hero .cta{position:absolute;left:388px;top:183px;background:var(--red);color:#fff;font-family:"Open Sans",Arial,sans-serif;font-weight:700;font-size:12px;padding:5px 10px}
.hero .arrow{position:absolute;top:108px}
.hero .arrow.prev{left:14px}
.hero .arrow.next{right:14px}
.dots{display:flex;justify-content:center;gap:3px;margin-top:4px}
.dots span{width:10px;height:10px;border-radius:50%;border:1px solid #aaa;background:#e8e8e8}
.dots span:first-child{background:#fff}
.section-title{font-family:"PT Sans",Arial,sans-serif;font-weight:400;font-size:13px;color:#333;margin:22px 0 0 16px}
.products{display:flex;gap:14px;margin:13px 13px 0}
.card{position:relative;width:140px;height:204px;border:1px solid var(--line);padding:8px 8px 0}
.card.hover{border-color:#b9d9f2}
.card .image{height:120px;border:1px solid var(--line);background:#fff;position:relative}
.card .image::before{content:"";position:absolute;left:14px;top:12px;right:14px;bottom:12px;border-radius:10px;background:radial-gradient(ellipse at 50% 45%,var(--garment) 0%,var(--garment) 55%,rgba(255,255,255,0) 100%)}
.image.tee-teal{--garment:var(--tee-teal)}
.image.rugby-green{--garment:var(--rugby-green)}
.image.tee-green{--garment:var(--tee-green)}
.image.sweat-lilac{--garment:var(--sweat-lilac)}
.image.dress-lilac{--garment:var(--dress-lilac)}
.image.dress-plum{--garment:var(--dress-plum)}
.image.dress-dots{--garment:var(--dress-dots)}
.image.dress-coral{--garment:var(--dress-coral)}
.card .name{font-weight:700;font-size:7.5px;margin-top:16px}
.card .price{font-size:7.5px;margin-top:5px}
.card .price s{color:#aaa;margin-right:3px}
.card .price em{font-style:normal;color:var(--sale)}
.card .actions{display:flex;align-items:center;margin-top:12px}
.card .btn{border:1px solid #ddd;background:#f7f7f7;font-size:7px;padding:3px 6px;border-radius:2px}
.card .icons{margin-left:auto;display:flex;gap:6px}
.card .tip{position:absolute;right:9px;bottom:30px;background:#333;color:#fff;font-size:6.5px;padding:2px 5px;border-radius:2px}
.band{position:absolute;left:0;top:953px;width:632px;height:19px;background:var(--sky)}
.footer{position:absolute;left:0;top:972px;width:632px;height:148px;display:flex}
.footer .col{flex:1;padding:14px 14px;border-right:1px solid var(--line)}
.footer .col:last-child{border-right:0}
.footer h3{font-family:"PT Sans",Arial,sans-serif;font-weight:400;font-size:12px;color:#333;margin-bottom:9px}
.footer p{font-size:7px;line-height:10.5px;color:#777}
.footer p a{color:var(--sale);font-style:italic;font-weight:700;text-decoration:none}
.footer .finder{display:flex;gap:4px;margin-top:11px}
.footer .finder .field{width:160px;height:24px;border:1px solid #ddd;font-size:7px;color:#aaa;font-style:italic;padding:7px 8px}
.footer .finder .go{width:26px;height:24px;border:1px solid #ddd;font-size:7px;color:#999;display:flex;align-items:center;justify-content:center}
.footer .social{display:flex;gap:5px;margin-top:10px}
.footer .social span{width:20px;height:20px;border-radius:2px}
.copyright{position:absolute;left:0;top:1120px;width:632px;border-top:1px solid var(--line);font-size:7px;padding:12px 14px}
</style>
</head>
<body>
<div class="page">
  <header>
    <div class="topbar">
      <div class="item"><svg width="8" height="8" viewBox="0 0 8 8"><circle cx="4" cy="2.5" r="2" fill="#ccc"/><path d="M0 8c0-3 8-3 8 0z" fill="#ccc"/></svg>My Account</div>
      <div class="item"><svg width="10" height="8" viewBox="0 0 10 8"><path d="M0 1h2l1.5 4.5h5L10 2H3" fill="none" stroke="#ccc"/><circle cx="4" cy="7" r="1" fill="#ccc"/><circle cx="8" cy="7" r="1" fill="#ccc"/></svg>Shopping Cart</div>
      <div class="checkout">Checkout</div>
      <div class="welcome">Welcome visitor you can <a>login</a> or <a>create an account</a></div>
    </div>
    <div class="masthead">
      <div class="logo">LOGO<span>HERE</span></div>
      <div class="cart">
        <div><div class="label">Shopping Cart</div><div class="count">0 item(s)</div></div>
        <div class="total">$1280.00</div>
      </div>
    </div>
    <nav class="nav">
      <div class="home"><svg width="10" height="9" viewBox="0 0 10 9"><path d="M5 0L0 4.5h1.5V9h2.5V6h2v3h2.5V4.5H10z" fill="#fff"/></svg></div>
      <a class="active">Boys Clothing</a><a>Girls Clothing</a><a>Our Brands</a><a>About Us</a><a>Contact Us</a>
      <div class="search">Search<div class="field"><svg width="8" height="8" viewBox="0 0 8 8"><circle cx="3.2" cy="3.2" r="2.4" fill="none" stroke="#aaa"/><path d="M5 5l2.5 2.5" stroke="#aaa"/></svg></div></div>
    </nav>
  </header>

  <section class="hero">
    <div class="inner">
      <div class="photo" role="img" aria-label="Photo of a smiling toddler in glasses and a striped jumper"></div>
      <div class="brand">Tiny Fair</div>
      <div class="headline">SNEAK PEEK</div>
      <div class="sub">into all infant essentials</div>
      <div class="list">Clothing | Outdoor Gear | Bath &amp; Skin Care<br>Diapering | Child Proofing</div>
      <div class="cta">Shop Now ▸</div>
    </div>
    <svg class="arrow prev" width="10" height="16" viewBox="0 0 10 16"><path d="M8 1L2 8l6 7" fill="none" stroke="#bbb" stroke-width="2"/></svg>
    <svg class="arrow next" width="10" height="16" viewBox="0 0 10 16"><path d="M2 1l6 7-6 7" fill="none" stroke="#bbb" stroke-width="2"/></svg>
  </section>
  <div class="dots"><span></span><span></span><span></span><span></span><span></span></div>

  <h2 class="section-title">Boys Clothing</h2>
  <div class="products">
    <div class="card"><div class="image tee-teal" role="img" aria-label="Photo of a dark teal long-sleeve boys tee with a printed graphic"></div><div class="name">Product Name</div><div class="price">$500.00</div><div class="actions"><span class="btn">Add to cart</span><span class="icons"><svg width="8" height="7"><path d="M1 7V4M4 7V1M7 7V3" stroke="#bbb" stroke-width="1.6"/></svg><svg width="8" height="7" viewBox="0 0 8 7"><path d="M4 7L.5 3.2A1.8 1.8 0 014 1a1.8 1.8 0 013.5 2.2z" fill="#ccc"/></svg></span></div></div>
    <div class="card hover"><div class="image rugby-green" role="img" aria-label="Photo of a green and navy striped boys rugby shirt"></div><div class="name">Product Name</div><div class="price"><s>$500.00</s><em>$400.00</em></div><div class="actions"><span class="btn">Add to cart</span><span class="icons"><svg width="8" height="7"><path d="M1 7V4M4 7V1M7 7V3" stroke="#3ba6dc" stroke-width="1.6"/></svg><svg width="8" height="7" viewBox="0 0 8 7"><path d="M4 7L.5 3.2A1.8 1.8 0 014 1a1.8 1.8 0 013.5 2.2z" fill="#ccc"/></svg></span></div><div class="tip">Compare</div></div>
    <div class="card"><div class="image tee-green" role="img" aria-label="Photo of a bright green boys t-shirt"></div><div class="name">Product Name</div><div class="price">$500.00</div><div class="actions"><span class="btn">Add to cart</span><span class="icons"><svg width="8" height="7"><path d="M1 7V4M4 7V1M7 7V3" stroke="#bbb" stroke-width="1.6"/></svg><svg width="8" height="7" viewBox="0 0 8 7"><path d="M4 7L.5 3.2A1.8 1.8 0 014 1a1.8 1.8 0 013.5 2.2z" fill="#ccc"/></svg></span></div></div>
    <div class="card"><div class="image sweat-lilac" role="img" aria-label="Photo of a lavender boys sweatshirt with a navy print"></div><div class="name">Product Name</div><div class="price"><s>$500.00</s><em>$400.00</em></div><div class="actions"><span class="btn">Add to cart</span><span class="icons"><svg width="8" height="7"><path d="M1 7V4M4 7V1M7 7V3" stroke="#bbb" stroke-width="1.6"/></svg><svg width="8" height="7" viewBox="0 0 8 7"><path d="M4 7L.5 3.2A1.8 1.8 0 014 1a1.8 1.8 0 013.5 2.2z" fill="#ccc"/></svg></span></div></div>
  </div>

  <h2 class="section-title">Girls Clothing</h2>
  <div class="products">
    <div class="card"><div class="image dress-lilac" role="img" aria-label="Photo of a purple gingham girls sundress"></div><div class="name">Product Name</div><div class="price">$500.00</div><div class="actions"><span class="btn">Add to cart</span><span class="icons"><svg width="8" height="7"><path d="M1 7V4M4 7V1M7 7V3" stroke="#bbb" stroke-width="1.6"/></svg><svg width="8" height="7" viewBox="0 0 8 7"><path d="M4 7L.5 3.2A1.8 1.8 0 014 1a1.8 1.8 0 013.5 2.2z" fill="#ccc"/></svg></span></div></div>
    <div class="card"><div class="image dress-plum" role="img" aria-label="Photo of a dark purple tulle party dress"></div><div class="name">Product Name</div><div class="price"><s>$500.00</s><em>$400.00</em></div><div class="actions"><span class="btn">Add to cart</span><span class="icons"><svg width="8" height="7"><path d="M1 7V4M4 7V1M7 7V3" stroke="#3ba6dc" stroke-width="1.6"/></svg><svg width="8" height="7" viewBox="0 0 8 7"><path d="M4 7L.5 3.2A1.8 1.8 0 014 1a1.8 1.8 0 013.5 2.2z" fill="#ccc"/></svg></span></div><div class="tip">Compare</div></div>
    <div class="card"><div class="image dress-dots" role="img" aria-label="Photo of a white polka-dot dress with pink flowers and bow"></div><div class="name">Product Name</div><div class="price">$500.00</div><div class="actions"><span class="btn">Add to cart</span><span class="icons"><svg width="8" height="7"><path d="M1 7V4M4 7V1M7 7V3" stroke="#bbb" stroke-width="1.6"/></svg><svg width="8" height="7" viewBox="0 0 8 7"><path d="M4 7L.5 3.2A1.8 1.8 0 014 1a1.8 1.8 0 013.5 2.2z" fill="#ccc"/></svg></span></div></div>
    <div class="card"><div class="image dress-coral" role="img" aria-label="Photo of a pink striped girls dress with floral collar"></div><div class="name">Product Name</div><div class="price"><s>$500.00</s><em>$400.00</em></div><div class="actions"><span class="btn">Add to cart</span><span class="icons"><svg width="8" height="7"><path d="M1 7V4M4 7V1M7 7V3" stroke="#bbb" stroke-width="1.6"/></svg><svg width="8" height="7" viewBox="0 0 8 7"><path d="M4 7L.5 3.2A1.8 1.8 0 014 1a1.8 1.8 0 013.5 2.2z" fill="#ccc"/></svg></span></div></div>
  </div>

  <div class="band"></div>
  <footer class="footer">
    <div class="col">
      <h3>WHO WE ARE</h3>
      <p>Pellentesque habitant morbi tristique senectus et netus et malesuada fames ac turpis egestas. Vestibulum tortor quam, feugiat vitae, ultricies eget, tempor sit amet, ante. Donec eu libero sit amet quam egestas semper. Aenean ultricies mi vitae est. Mauris placerat eleifend leo. Quisque sit amet est et sapien ullamcorper pharetra. <a>Read More</a></p>
    </div>
    <div class="col">
      <h3>FIND SOMETHING</h3>
      <p>Pellentesque habitant morbi tristique senectus et netus et malesuada fames.</p>
      <div class="finder"><div class="field">Looking for Something?</div><div class="go">GO</div></div>
    </div>
    <div class="col">
      <h3>SOCIAL CONNECTIONS</h3>
      <p>Pellentesque habitant morbi tristique senectus et netus et malesuada fames.</p>
      <div class="social"><span style="background:#3b5998"></span><span style="background:#33b5e5"></span><span style="background:#d9332b"></span></div>
    </div>
  </footer>
  <div class="copyright">Copyright © 2013.</div>
</div>
</body>
</html>
```